Packaging Design for Premium Airlink Speaker

I need the packaging 3D design for a mini bluetooth speaker, with the exterior graphic design as well. We need the look and feel of the packaging to appeal to premium customers. Since we will undercut the price of other premium bluetooth speakers but need to make sure that the packaging evokes quality so that our customers don't feel they are settling for something cheaper. We will be competing with speakers such as the tunra orb and the velko petite bluetooth speaker (you can review those packages on videos online for reference). We are looking for an innovative design, but with down to earth inexpensive materials. The dimensions of the bluetooth speaker are the following: Length 189 mm x width 55 mm x Height 80mm. A small space is also required for the manual/warrantee, and for 2 small cables (a USB charging cable and an aux cable with a 3.5 mm jack). The bluetooth speaker is natural aluminum and we can provide photos (attached). The speaker we will sell is the silver aluminum one. This is our first experience with ArtHivery. This is a youtube link of a similar speaker with a nice design: https://www.vidplume.example/watch?v=q7TzLmNaPoR
We can be more playful with our design, but making sure it is still elegant. However, this design exemplifies the inner compartments we would like to have.

Target Market(s)

People that cannot afford the premium brands (VELKO, MR. KAL TUNRA, HUMCRATE) but like a great speaker with premium look and feel. Our MSRP will be arround $99 - $119 USD (the premium brands cost $200 or more).

Industry/Entity Type

Graphic Design

Font styles to use
Sans Serif

Requirements
Must have
• The packaging outer design should contain space for a barcode, the logo of our brand: Linden Sonics, which has not been designed AND needs to be designed as well, and space for specs and info (you can place basic information of about 2 paragraphs and we can populate later with the actual info).
Nice to have
• The interior should be well protected and have compartments for the speaker, the cables, and the manual. The designer has creative discretion over colors and spacing, but keep in mind it needs to evoke quality and premium feel.

```html
<!DOCTYPE html>
<html lang="en">
<head>
<meta charset="utf-8">
<title>Linden Sonics – mini airlink speaker packaging</title>
<link rel="stylesheet" href="https://fonts.googleapis.com/css2?family=Exo+2:ital,wght@0,800;1,500&family=Roboto+Condensed:wght@700&display=swap">
<style>
  :root {
    --backdrop: #1e1e1e;
    --silver-light: #f4f6f8;
    --silver-mid: #c9c7c4;
    --silver-shade: #a9a6a2;
    --side-light: #f1f5f8;
    --side-shade: #d5d7d9;
    --ink: #161616;
    --paper: #ffffff;
    --rule: #8f8c88;
    --badge-blue: #1f4f9a;
  }
  * { margin: 0; padding: 0; box-sizing: border-box; }
  html, body {
    width: 1200px;
    height: 927px;
    overflow: hidden;
    background: var(--backdrop);
  }
  .canvas {
    position: relative;
    width: 1200px;
    height: 927px;
  }
  .box {
    position: absolute;
    left: 180px;
    top: 233px;
    width: 840px;
    height: 460px;
    display: flex;
  }
  .box-side {
    width: 150px;
    height: 100%;
    background: linear-gradient(90deg, var(--side-shade) 0%, var(--side-light) 35%, var(--side-light) 70%, var(--side-shade) 100%);
    border-right: 1px solid var(--silver-shade);
  }
  .box-front {
    position: relative;
    width: 690px;
    height: 100%;
    background:
      linear-gradient(115deg, var(--silver-shade) 0%, var(--silver-mid) 22%, var(--silver-light) 52%, var(--silver-mid) 78%, var(--silver-shade) 100%);
    overflow: hidden;
  }
  .tagline {
    position: absolute;
    left: 85px;
    top: 150px;
    font-family: "Exo 2", sans-serif;
    font-style: italic;
    font-weight: 500;
    font-size: 30px;
    letter-spacing: 1px;
    color: var(--paper);
    white-space: nowrap;
  }
  .brand-name {
    position: absolute;
    left: 82px;
    top: 210px;
    font-family: "Exo 2", sans-serif;
    font-weight: 800;
    font-size: 72px;
    line-height: 1;
    color: var(--ink);
    white-space: nowrap;
  }
  .band-rule {
    position: absolute;
    left: 0;
    right: 0;
    top: 355px;
    height: 1px;
    background: var(--rule);
    opacity: 0.6;
  }
  .info-band {
    position: absolute;
    left: 0;
    right: 0;
    top: 356px;
    bottom: 0;
    display: flex;
    align-items: center;
    padding: 0 40px 0 20px;
  }
  .circuit-mark {
    width: 90px;
    height: 40px;
    background: linear-gradient(90deg, #d6d4d1, #bfbcb8);
    border-radius: 3px;
  }
  .wireless-badge {
    display: flex;
    align-items: center;
    gap: 10px;
    margin-left: 14px;
  }
  .wireless-badge .dot {
    width: 30px;
    height: 30px;
    border-radius: 50%;
    background: var(--badge-blue);
  }
  .wireless-badge .label {
    font-family: "Roboto Condensed", sans-serif;
    font-weight: 700;
    font-size: 28px;
    color: var(--ink);
  }
  .controls {
    margin-left: auto;
    display: flex;
  }
</style>
</head>
<body>
<main class="canvas">
  <div class="box">
    <section class="box-side" aria-label="Box side panel"></section>
    <section class="box-front">
      <p class="tagline">mini airlink speaker</p>
      <h1 class="brand-name">Linden Sonics</h1>
      <div class="band-rule"></div>
      <div class="info-band">
        <div class="circuit-mark" role="img" aria-label="Small logic gate schematic with inputs A and B and output Y"></div>
        <div class="wireless-badge">
          <span class="dot"></span>
          <span class="label">Airlink</span>
        </div>
        <svg class="controls" width="150" height="40" viewBox="0 0 150 40" aria-label="Four speaker control buttons" role="img">
          <defs>
            <radialGradient id="knob" cx="50%" cy="45%" r="55%">
              <stop offset="0" stop-color="#ffffff"/>
              <stop offset="0.5" stop-color="#b9b9b9"/>
              <stop offset="0.8" stop-color="#e8e8e8"/>
              <stop offset="1" stop-color="#7d7d7d"/>
            </radialGradient>
          </defs>
          <circle cx="18" cy="20" r="16" fill="url(#knob)" stroke="#8a8a8a"/>
          <circle cx="56" cy="21" r="15" fill="url(#knob)" stroke="#8a8a8a"/>
          <circle cx="92" cy="21" r="14" fill="url(#knob)" stroke="#8a8a8a"/>
          <circle cx="126" cy="21" r="13" fill="url(#knob)" stroke="#8a8a8a"/>
        </svg>
      </div>
    </section>
  </div>
</main>
</body>
</html>
```